Logo-Briefpapier-Visitenkarte für Beratungsunternehmen
Zielgruppe
kleine und Kleinstunternehmer aller Branchen; kleine Unternehmen wie z.B. Friseure, Bäcker, Groß- und Einzelhändler, Handwerker, Floristen, Manufakturen, etc., die Unterstützung und Beratung für ihre Unternehmung wünschen (z.B. Buchhaltung, Jahresabschluss, Steuerberatung, Controlling; Marketing-, Vertriebs-, Organisationsberatung, Prozessgestaltung)
Aufgabenstellung
Erstellung des Designs von Logo, Briefpapier, Visitenkarte(n)
Inhalt Logo: mindestens Namen und Untertitel ("Die Unternehmerpartner")
Inhalt Briefpapier: Logo, Firmenname inkl. Untertitel ("Die Unternehmerpartner"), Kontaktdaten.
Inhalt Visitenkarte: Logo, Firmenname inkl. Untertitel ("Die Unternehmerpartner"), Kontaktdaten inkl. Titel, Berufsbezeichnung, Telefon, email,etc.

```html
<!DOCTYPE html>
<html lang="de">
<head>
<meta charset="utf-8">
<title>Brunnhof Beratung – Geschäftsausstattung</title>
<link rel="stylesheet" href="https://fonts.googleapis.com/css2?family=Alegreya:wght@400;700&display=swap">
<style>
  :root {
    --board: #ffffff;
    --ink: #1a1a1a;
    --dark-1: #2e2e2e;
    --dark-2: #050505;
    --logo-light: #d6d6d6;
    --subtitle-light: #bdbdbd;
    --paper: #ffffff;
    --card-light-1: #ffffff;
    --card-light-2: #c9c9c9;
    --shadow: rgba(0, 0, 0, 0.45);
  }
  * { box-sizing: border-box; margin: 0; padding: 0; }
  html, body { width: 1200px; height: 900px; overflow: hidden; background: var(--board); }
  body { position: relative; font-family: "Alegreya", Georgia, serif; color: var(--ink); }
  address { font-style: normal; }

  .brand-name { font-weight: 400; line-height: 1; white-space: nowrap; }
  .brand-claim { font-weight: 400; line-height: 1.1; white-space: nowrap; }

  /* Letterhead */
  .letterhead {
    position: absolute; left: 506px; top: 41px; width: 582px; height: 820px;
    background: var(--paper); box-shadow: 3px 4px 6px var(--shadow);
  }
  .letterhead-band {
    height: 117px; padding: 30px 0 0 40px;
    background: radial-gradient(ellipse at 50% 120%, var(--dark-1), var(--dark-2) 70%);
  }
  .letterhead-band .brand-name { font-size: 35px; color: var(--logo-light); }
  .letterhead-band .brand-claim { font-size: 13px; color: var(--subtitle-light); margin-top: 3px; }
  .sender-line { position: absolute; left: 40px; top: 168px; font-size: 6px; }
  .letter-body { position: absolute; left: 40px; top: 366px; width: 380px; font-size: 8.6px; line-height: 11.6px; }
  .letter-body p { margin-bottom: 11.6px; }
  .letter-contact { position: absolute; right: 20px; top: 697px; text-align: right; font-size: 8.6px; line-height: 11.6px; }
  .letter-contact p + p { margin-top: 11.6px; }

  /* Business cards */
  .card { position: absolute; box-shadow: 3px 4px 6px var(--shadow); }
  .card-front {
    background: radial-gradient(ellipse at 45% 110%, var(--dark-1), var(--dark-2) 72%);
  }
  .card-front .brand-name { color: var(--logo-light); }
  .card-front .brand-claim { color: var(--subtitle-light); }

  .card-small { width: 281px; height: 176px; }
  .card-small-front { left: 134px; top: 146px; transform: rotate(-8deg); padding: 68px 0 0 28px; }
  .card-small-front .brand-name { font-size: 27px; }
  .card-small-front .brand-claim { font-size: 10px; margin-top: 2px; }

  .card-back {
    left: 186px; top: 316px; transform: rotate(8deg);
    background: radial-gradient(ellipse at 40% 30%, var(--card-light-1), var(--card-light-2) 90%);
    padding: 18px 20px 0 22px;
  }
  .card-back .brand-name { font-size: 15px; }
  .card-back .brand-claim { font-size: 5px; }
  .card-back-contact { position: absolute; right: 20px; top: 56px; text-align: right; font-size: 8.6px; line-height: 10.5px; }
  .card-back-contact p + p { margin-top: 8px; }

  .card-large { left: 21px; top: 541px; width: 551px; height: 346px; padding: 134px 0 0 64px; }
  .card-large .brand-name { font-size: 52px; }
  .card-large .brand-claim { font-size: 17px; margin-top: 4px; }
</style>
</head>
<body>

<article class="letterhead">
  <header class="letterhead-band">
    <div class="brand-name">Brunnhof Beratung</div>
    <div class="brand-claim">Partner für kleine Betriebe</div>
  </header>
  <div class="sender-line">Brunnhof Beratung · Lindenweg 14 · 55671 Musterfeld</div>
  <div class="letter-body">
    <p>Lorem ipsum dolor sit amet, consectetuer adipiscing elit. Aenean commodo ligula eget dolor. Aenean massa. Cum sociis natoque penatibus et magnis dis parturient montes, nascetur ridiculus mus. Donec quam felis, ultricies nec, pellentesque eu, pretium quis, sem. Nulla consequat massa quis enim. Donec pede justo, fringilla vel, aliquet nec, vulputate eget, arcu.</p>
    <p>In enim justo, rhoncus ut, imperdiet a, venenatis vitae, justo. Nullam dictum felis eu pede mollis pretium. Integer tincidunt. Cras dapibus. Vivamus elementum semper nisi. Aenean vulputate eleifend tellus. Aenean leo ligula, porttitor eu, consequat vitae, eleifend ac, enim. Aliquam lorem ante, dapibus in, viverra quis, feugiat a, tellus.</p>
    <p>Phasellus viverra nulla ut metus varius laoreet. Quisque rutrum. Aenean imperdiet. Etiam ultricies nisi vel augue. Curabitur ullamcorper ultricies nisi. Nam eget dui. Etiam rhoncus. Maecenas tempus, tellus eget condimentum rhoncus, sem quam semper libero, sit amet adipiscing sem neque sed ipsum. Nam quam nunc, blandit vel, luctus pulvinar, hendrerit id, lorem. Maecenas nec odio et ante tincidunt tempus. Donec vitae sapien ut libero venenatis faucibus. Nullam quis ante. Etiam sit amet orci eget eros faucibus tincidunt. Duis leo.</p>
    <p>Sed fringilla</p>
  </div>
  <address class="letter-contact">
    <p>Brunnhof Beratung<br>Lindenweg 14<br>55671 Musterfeld</p>
    <p>Telefon: 0261 / 480 352<br>Fax: 0261 / 480 353</p>
    <p>Email: info@brunnhof-beratung.de<br>Web: www.brunnhof-beratung.de</p>
  </address>
</article>

<section class="card card-small card-front card-small-front">
  <div class="brand-name">Brunnhof Beratung</div>
  <div class="brand-claim">Partner für kleine Betriebe</div>
</section>

<section class="card card-small card-back">
  <div class="brand-name">Brunnhof Beratung</div>
  <div class="brand-claim">Partner für kleine Betriebe</div>
  <address class="card-back-contact">
    <p>Brunnhof Beratung<br>Lindenweg 14<br>55671 Musterfeld</p>
    <p>Telefon: 0261 / 480 352<br>Fax: 0261 / 480 353</p>
    <p>Email: info@brunnhof-beratung.de<br>Web: www.brunnhof-beratung.de</p>
  </address>
</section>

<section class="card card-front card-large">
  <div class="brand-name">Brunnhof Beratung</div>
  <div class="brand-claim">Partner für kleine Betriebe</div>
</section>

</body>
</html>
```